Bao Lotus Menu Design Project

This project is pretty straight forward. You will be given 3 files which include the following:
1. Our proposed menu
2. Our Company logo
3. A sample menu on what we are looking for design wise

Your job is to create a visually pleasing menu that is simple, clean and fresh. Please refer to our home website for additional information. (www.baolotus-example.com) Must be in eps or equivalent format.

Target Market(s)

20s to 40s

Industry/Entity Type

It Company

Requirements
Must have
• Company log
Must be in EPS format

```html
<!DOCTYPE html>
<html lang="en">
<head>
<meta charset="utf-8">
<title>Bao Lotus Menu</title>
<link rel="stylesheet" href="https://fonts.googleapis.com/css2?family=Fira+Sans+Extra+Condensed:ital,wght@0,400;0,700;1,400&display=swap">
<style>
  :root {
    --canvas: #4a4a4a;
    --page: #1d1b1e;
    --ink: #f3ead2;
    --heading: #ffffff;
    --accent: #e3051b;
    --photo-top: rgba(29,27,30,0);
    --photo-mid: #3a2a1f;
    --photo-low: #22170f;
  }
  * { box-sizing: border-box; margin: 0; padding: 0; }
  html, body { width: 1200px; height: 900px; overflow: hidden; background: var(--canvas); }
  body { position: relative; font-family: "Fira Sans Extra Condensed", "Arial Narrow", sans-serif; color: var(--ink); }

  .menu-page {
    position: absolute; top: 99px; width: 543px; height: 702px;
    background: var(--page); overflow: hidden;
  }
  .menu-page--left { left: 43px; }
  .menu-page--right { left: 615px; }

  .interior-photo {
    position: absolute; left: 0; right: 0; top: 360px; bottom: 39px;
    background:
      radial-gradient(ellipse at 45% 60%, rgba(120,80,45,.45), rgba(0,0,0,0) 60%),
      linear-gradient(180deg, var(--photo-top) 0%, var(--photo-mid) 45%, var(--photo-low) 100%);
  }
  .accent-band { position: absolute; left: 0; right: 0; bottom: 0; height: 39px; background: var(--accent); }

  .brand-name {
    position: absolute; right: 40px; bottom: 56px;
    font-weight: 700; font-size: 16px; line-height: 1;
    color: var(--heading); letter-spacing: .3px; white-space: nowrap;
  }

  .menu-column { position: absolute; top: 47px; width: 156px; text-align: center; }
  .section-title { font-weight: 700; font-size: 14.5px; color: var(--heading); letter-spacing: .4px; margin-bottom: 6px; }
  .section-note { font-size: 8.4px; line-height: 1.32; font-style: italic; margin-top: -3px; margin-bottom: 8px; }
  .section-note--plain { font-style: normal; }
  .menu-item { margin-bottom: 9px; }
  .item-name { font-weight: 700; font-size: 9px; text-transform: uppercase; line-height: 1.3; }
  .item-price { font-weight: 700; font-size: 9px; line-height: 1.35; }
  .item-desc { font-size: 8px; line-height: 1.35; }
  .section-gap { margin-top: 22px; }
</style>
</head>
<body>

<section class="menu-page menu-page--left" aria-label="Menu page one">
  <div class="interior-photo" role="img" aria-label="Dim restaurant interior with booths and a set table"></div>
  <div class="accent-band"></div>
  <p class="brand-name">Bao Lotus</p>

  <div class="menu-column" style="left:29px">
    <h2 class="section-title">DIM SUM</h2>
    <div class="menu-item"><p class="item-name">Pan-Fried Potstickers</p><p class="item-price">- 6.50</p><p class="item-desc">Five pan-fried potstickers with chicken or pork. Served with apricot dipping sauce.</p></div>
    <div class="menu-item"><p class="item-name">Steamed Dumplings</p><p class="item-price">- 6.50</p><p class="item-desc">Five steamed dumplings with chicken, or vegetables. Served with apricot dipping sauce.</p></div>
    <div class="menu-item"><p class="item-name">Szechuan Dumplings</p><p class="item-price">- 6.25</p><p class="item-desc">Five chicken dumplings tossed in a spicy cilantro sauce.</p></div>
    <div class="menu-item"><p class="item-name">Spring Rolls</p><p class="item-price">- 4.50</p><p class="item-desc">Two chicken or vegetable spring rolls. Served with apricot dipping sauce.</p></div>
    <div class="menu-item"><p class="item-name">Wonton Stars</p><p class="item-price">- 7.25</p><p class="item-desc">Five crispy wonton skins filled with real crab and seasoned cream cheese. Served with sweet and sour dipping sauce.</p></div>
    <div class="menu-item"><p class="item-name">Bao</p><p class="item-price">- 5.95</p><p class="item-desc">Three fluffy steamed chinese buns filled with barbeque pork.</p></div>
    <div class="menu-item"><p class="item-name">Shrimp Toast</p><p class="item-price">- 5.95</p><p class="item-desc">Four pieces of fried toast with shrimp, onions, bamboo shoots, and water chestnuts. Served with apricot dipping sauce.</p></div>
    <div class="menu-item"><p class="item-name">Shu Mai</p><p class="item-price">- 5.95</p><p class="item-desc">Six steamed open-face dumplings with pork, shrimp, and mushrooms.</p></div>
    <div class="menu-item"><p class="item-name">Gift Wrapped Chicken</p><p class="item-price">- 5.95</p><p class="item-desc">Six chicken breast tenders marinated in soy sauce, sesame oil, and cilantro.</p></div>
    <div class="menu-item"><p class="item-name">Assorted Pleasures</p><p class="item-price">- 8.95</p><p class="item-desc">Two chicken potstickers, two fried chicken wontons, two gift wrapped chicken, and one vegetable spring roll.</p></div>
  </div>

  <div class="menu-column" style="left:194px">
    <h2 class="section-title">STARTERS</h2>
    <div class="menu-item"><p class="item-name">Edamame</p><p class="item-price">- 4.00</p><p class="item-desc">Steamed Soybean Pods.</p></div>
    <div class="menu-item"><p class="item-name">Lightly Battered Calamari Strips</p><p class="item-price">- 5.95</p><p class="item-desc">Six calamari strips, lightly battered with a garlic ginger aioli.</p></div>
    <div class="menu-item"><p class="item-name">4 C's Bao Lotus Crab Cake's</p><p class="item-price">- 11.95</p><p class="item-desc">Jumbo lump Maryland crab meat with seasoned with our Bao Lotus spice blend. Topped with a kick of spicy aioli.</p></div>
    <h2 class="section-title">LUNCH / DINNER</h2>
    <div class="menu-item"><p class="item-name">Dim Sum and Then Sum</p><p class="item-price">- 14.95 / 18.95</p><p class="item-desc">Choose three / four half orders: Potstickers, steamed dumplings, szechwan dumplings, spring roll, shrimp toast, chinese chicken salad, hot &amp; sour soup, wonton soup, or mushu. For Shrimp fried rice, beef fried rice, or mushu shrimp, add $1.00.</p></div>
    <h2 class="section-title section-gap">SOUP</h2>
    <div class="menu-item"><p class="item-name">Sm.&nbsp;&nbsp;&nbsp;Lg.</p><p class="item-name">Wonton Soup</p><p class="item-price">- 4.95&nbsp;&nbsp;7.50</p><p class="item-desc">Chicken or pork wonton dumplings with spinach and scallions in chicken broth.</p></div>
    <div class="menu-item"><p class="item-name">Miso Soup</p><p class="item-price">- 4.95&nbsp;&nbsp;7.50</p><p class="item-desc">Miso Based Soup with tofu and scallions</p></div>
    <div class="menu-item"><p class="item-name">Hot and Sour Soup</p><p class="item-price">- 4.95&nbsp;&nbsp;7.50</p><p class="item-desc">Shredded pork, scallions, carrots, egg, and soft tofu.</p></div>
    <div class="menu-item"><p class="item-name">Velvet Corn Soup</p><p class="item-price">- 7.25</p><p class="item-desc">Cellophane noodles, chicken, sweet corn, green peas, and egg. No modifications</p></div>
  </div>

  <div class="menu-column" style="left:358px">
    <h2 class="section-title">SALADS</h2>
    <p class="section-note section-note--plain">Can replace Chicken with Tofu for $1.50</p>
    <div class="menu-item"><p class="item-name">Chinese Chicken Salad</p><p class="item-price">- 10.50</p><p class="item-desc">Shredded lettuce, chicken breast, breast and vegetables in a spicy browncrunchies, and white crunchies with tart red ginger dressing</p></div>
    <div class="menu-item"><p class="item-name">Main Mein Salad</p><p class="item-price">- 9.95</p><p class="item-desc">Cold lo mein noodles with chicken breast, red cabbage, carrots, peanut dressing.</p></div>
    <div class="menu-item"><p class="item-name">Sesame Chicken Salad</p><p class="item-price">- 9.95</p><p class="item-desc">Shredded lettuce, chicken breast, red cabbage, carrots, browncrunchies, fresh oranges, scallions, and sesame dressing.</p></div>
  </div>
</section>

<section class="menu-page menu-page--right" aria-label="Menu page two">
  <div class="interior-photo" role="img" aria-label="Dim restaurant interior with booths and a set table"></div>
  <div class="accent-band"></div>
  <p class="brand-name">Bao Lotus</p>

  <div class="menu-column" style="left:28px">
    <h2 class="section-title">CHICKEN</h2>
    <p class="section-note">For white meat chicken, add $1.00.<br>Enjoy a Half Chinese Chicken Salad or Plain Fried Rice with any entrée for $5.50<br>Can replace Chicken with Tofu for $1.50</p>
    <div class="menu-item"><p class="item-name">Orange Chicken</p><p class="item-price">-11.95</p><p class="item-desc">Crispy chicken breast with onions and red and green bell peppers in a tangy orange sauce.</p></div>
    <div class="menu-item"><p class="item-name">General Tso's Chicken</p><p class="item-price">-11.75</p><p class="item-desc">Crispy dark meat chicken with chili peppers in a spicy tangerine sauce topped with scallions.</p></div>
    <div class="menu-item"><p class="item-name">Kung Pao Chicken</p><p class="item-price">-11.95</p><p class="item-desc">Dark meat chicken with red bell peppers, peanuts, and water chestnuts in spicy red sauce.</p></div>
    <div class="menu-item"><p class="item-name">Chicken Lettuce Cups</p><p class="item-price">-11.75</p><p class="item-desc">Minced white meat chicken with bell peppers, water chestnuts, black mushrooms, pine nuts, and white crunchies. Served with four lettuce cups.</p></div>
    <div class="menu-item"><p class="item-name">Chicken with Asparagus</p><p class="item-price">-11.95</p><p class="item-desc">Chicken breast with asparagus and carrots in a lemon white wine sauce.</p></div>
    <div class="menu-item"><p class="item-name">Chicken with Snow Peas</p><p class="item-price">-11.75</p><p class="item-desc">Chicken breast served with snow peas, fresh mushrooms, carrots, and sliced garlic.</p></div>
    <div class="menu-item"><p class="item-name">Teriyaki Chicken Bowl</p><p class="item-price">-11.95</p><p class="item-desc">Dark meat chicken glazed in Teriyaki sauce placed over a bed of rice.</p></div>
    <div class="menu-item"><p class="item-name">Tangerine Chicken</p><p class="item-price">-11.75</p><p class="item-desc">Crispy chicken breast topped with scallions in a tangerine sauce.</p></div>
    <div class="menu-item"><p class="item-name">Almond Chicken</p><p class="item-price">-11.95</p><p class="item-desc">Dark meat chicken with bamboo shoots, celery, water chestnuts, and toasted almonds. Prepared regularly or mandarin-Style.</p></div>
  </div>

  <div class="menu-column" style="left:193px">
    <h2 class="section-title">CHICKEN</h2>
    <div class="menu-item"><p class="item-name">Lemon Chicken</p><p class="item-price">-11.75</p><p class="item-desc">Crispy chicken breast marinated in garlic and ginger; served with a tart lemon sauce on the side.</p></div>
    <div class="menu-item"><p class="item-name">Cashew Chicken</p><p class="item-price">-11.95</p><p class="item-desc">Chicken breast, zucchini, onions, garlic, ginger, and cashews tossed in an oyster sauce.</p></div>
    <div class="menu-item"><p class="item-name">Curry Chicken</p><p class="item-price">-11.95</p><p class="item-desc">Chicken breast with potatoes, onions, green peas, and carrots in a curry sauce.</p></div>
    <div class="menu-item"><p class="item-name">Sweet and Sour Chicken</p><p class="item-price">-11.50</p><p class="item-desc">Crispy chicken breast, bell peppers, onions, and pineapple in a sweet and sour sauce.</p></div>
  </div>

  <div class="menu-column" style="left:357px">
    <h2 class="section-title">BEEF &amp; PORK</h2>
    <p class="section-note">Rice is not included. Add rice $1.25.<br>Enjoy a Half Chinese Chicken Salad or Plain Fried Rice with any entrée for $5.50<br>Can replace Beef/Pork with Tofu for $1.50</p>
    <div class="menu-item"><p class="item-name">Mongolian Beef</p><p class="item-price">-12.25</p><p class="item-desc">Flank steak, garlic, ginger, and green onions on a bed of white crunchies.</p></div>
    <div class="menu-item"><p class="item-name">Beef and Broccoli</p><p class="item-price">-11.95</p><p class="item-desc">Flank steak, broccoli, and black mushrooms sautéed in a garlic brown sauce.</p></div>
    <div class="menu-item"><p class="item-name">Pepper Steak</p><p class="item-price">-11.95</p><p class="item-desc">Flank steak, bell peppers, onions, and garlic in black pepper sauce.</p></div>
    <div class="menu-item"><p class="item-name">Sliced Barbequed Pork</p><p class="item-price">-8.95</p><p class="item-desc">Tender slices of juicy pork topped with scallions in a barbeque sauce.</p></div>
    <div class="menu-item"><p class="item-name">Barbequed Spareribs</p><p class="item-price">-8.95</p><p class="item-desc">Slow-Roasted juicy pork ribs with barbeque sauce.</p></div>
    <div class="menu-item"><p class="item-name">Tangerine Beef</p><p class="item-price">-12.25</p><p class="item-desc">Crisp flank steak topped with scallions in a tangerine sauce.</p></div>
    <div class="menu-item"><p class="item-name">Spicy Garlic Tomato Beef</p><p class="item-price">-12.95</p><p class="item-desc">Flank steak, tomato, water chestnuts, zucchini, onions, and spicy garlic sauce.</p></div>
    <div class="menu-item"><p class="item-name">Ma Pao Tofu</p><p class="item-price">-7.95</p><p class="item-desc">Soft tofu cubes with ground pork or chicken cooked in Szechuan-Style sauce.</p></div>
  </div>
</section>

</body>
</html>
```